The Harlow Reserve Web Site design

I need a web design for my luxury range of Terry Toweling and Spa Accessories for luxury upmarket hotels and Spas. I have a catalog that sets the mood and tone I am looking for. I need a website design that shows off the look and feel of this luxury range while working back to the catalog look and feel. Its all about Upmarket and Luxury. I will be using the website as a reference site and as a site that customers can purchase off.
The Logo is attached as is the catalog. I don't mind changing the color of the Logo to match the website. However I would prefer to keep the font of that logo.

http://thegalleryloft.pixvaultex.com/p204519873
Please can you try and access this link. The Harlow Reserve
Name Bettina. Email bettina@kestrelsupplyco.com.au. Password Harlow.
These images are to be used for shopping page and please use the close up details of texture as background on pages and use those texture details and close ups for banners

Please note the look and feel has to be very upmarket and super luxury. Ficus is on mood and not on retail.
Have a look at the mood on the following websites
Www.gracefulretreatsex.com
And ourquietcovecottagestore.com
That one is retail .mi don't want retail focus but it's very clean. And simple and colors are good

Please rebook brief. I have added some important detail. Thanks

Relook brief. I have added,important detail. Thanks

Target Market(s)

Corporate buyers
This is not for retail selling to consumers
Price it's viewed only after secure login

Industry/Entity Type

Shopping

Colors
acd037
cadf82
fbc995
fce7d3
faa54b

Requirements
Must have
• Luxury. Think luxury. Very high end yet modern like the catalogue
Use banners on home page
Should not have
• Don't use the blue as the main color. It's too cheap.
No products on home page

```html
<!DOCTYPE html>
<html lang="en">
<head>
<meta charset="utf-8">
<title>The Harlow Reserve</title>
<link href="https://fonts.googleapis.com/css2?family=Pathway+Gothic+One&family=Roboto+Slab:wght@100;200;300;400&family=Arimo&display=swap" rel="stylesheet">
<style>
:root{
  --ink:#3a3a3a;
  --text:#7c7c7c;
  --soft:#9a9a9a;
  --white:#ffffff;
  --leaf:#acd037;
  --lime:#cadf82;
  --apricot:#fbc995;
  --blush:#fce7d3;
  --tangerine:#faa54b;
  --slab:"Roboto Slab", serif;
  --logo:"Pathway Gothic One", sans-serif;
  --sans:"Arimo", sans-serif;
}
*{margin:0;padding:0;box-sizing:border-box}
html,body{width:1029px;height:1200px;overflow:hidden;background:var(--white)}
body{position:relative;font-family:var(--slab);color:var(--text)}
.abs{position:absolute}

.brand{left:86px;top:28px;font-family:var(--logo);font-size:38px;line-height:46px;color:var(--ink);letter-spacing:.3px;word-spacing:4px;white-space:nowrap}

.account a{position:absolute;top:37px;font-size:12.5px;font-weight:300;color:var(--soft);text-decoration:none;white-space:nowrap}
.account .signin{left:490px;top:26px;width:118px;height:40px;background:linear-gradient(#fff 70%,var(--blush));box-shadow:0 3px 3px -2px rgba(0,0,0,.18);border-radius:2px}
.account .signin span{display:block;text-align:center;padding-top:11px;color:var(--ink);font-size:12.5px;font-weight:400}
.account .signin i{position:absolute;left:55px;bottom:-1px;border:4px solid transparent;border-bottom:0;border-top:5px solid var(--tangerine)}

.rule-dash{left:86px;width:857px;border-top:1px dashed var(--leaf)}
.main-nav{left:86px;top:107px;width:857px;height:14px;font-size:9.6px;color:var(--ink);letter-spacing:.2px}
.main-nav span{position:absolute;white-space:nowrap}
.main-nav .current{color:var(--leaf)}

.hero{left:86px;top:159px;width:857px;height:385px;overflow:hidden;
  background:linear-gradient(160deg,#7a6a55 0%,#6f7468 30%,#4f6a5e 55%,#2f3f3e 80%,#5b4b3a 100%)}
.hero .cloth{position:absolute;inset:0;background:linear-gradient(170deg,transparent 20%,rgba(215,210,198,.85) 45%,rgba(200,194,180,.8) 62%,transparent 80%)}
.hero .line1{position:absolute;left:54px;top:277px;font-size:28px;font-weight:200;color:var(--white);white-space:nowrap}
.hero .line2{position:absolute;left:22px;top:292px;font-size:72px;font-weight:100;color:var(--white);letter-spacing:11px;white-space:nowrap}

.intro-title{left:155px;top:584px;width:723px;display:flex;align-items:center;gap:18px;font-size:22px;font-weight:300;color:#6a6a6a;white-space:nowrap}
.intro-title::before,.intro-title::after{content:"";flex:1;border-top:1px solid var(--lime)}
.intro-text{left:155px;top:627px;width:723px;text-align:center;font-size:13.6px;line-height:22.4px;font-weight:300;color:var(--soft)}

.divider{left:160px;width:710px;height:14px}

.explore{left:0;width:1014px;top:784px;text-align:center;color:var(--ink)}
.explore .small{display:block;font-size:17px;font-weight:300;color:#555}
.explore .big{display:block;font-size:22px;font-weight:300;letter-spacing:1.5px;margin-top:-3px}

.textures .tile{position:absolute;top:843px;width:173px;height:86px}
.t1{left:159px;background:repeating-linear-gradient(90deg,#bcd65a 0 3px,var(--leaf) 3px 6px)}
.t2{left:340px;background:repeating-linear-gradient(45deg,var(--apricot) 0 4px,#f6b878 4px 8px)}
.t3{left:519px;background:repeating-linear-gradient(0deg,var(--blush) 0 4px,#f3d7bc 4px 8px)}
.t4{left:700px;background:repeating-linear-gradient(135deg,var(--tangerine) 0 4px,#ee9236 4px 8px)}
.textures .arrow{position:absolute;top:868px;font-family:var(--sans);font-size:30px;color:var(--tangerine)}

.partners span{position:absolute;top:998px;font-size:12px;font-weight:300;color:#8a8a8a;white-space:nowrap;letter-spacing:.5px}

.footer{left:86px;top:1090px;width:857px;height:60px;background:var(--blush);font-family:var(--sans);color:#444}
.footer .link{position:absolute;top:27px;font-size:9.4px;letter-spacing:.1px;white-space:nowrap}
.footer .social{position:absolute;top:23px;width:19px;height:19px;border-radius:2px;background:var(--tangerine)}
.footer address{position:absolute;left:574px;top:9px;font-style:normal;font-size:9.6px;line-height:15.6px;letter-spacing:.3px;white-space:nowrap}
</style>
</head>
<body>

<header>
  <div class="abs brand">The Harlow Reserve</div>
  <nav class="account">
    <a class="signin" href="#"><span>Sign in</span><i></i></a>
    <a href="#" style="left:638px">Register</a>
    <a href="#" style="left:738px">My Harlow</a>
    <a href="#" style="left:859px">My Wish List</a>
  </nav>
  <div class="abs rule-dash" style="top:88px"></div>
  <nav class="abs main-nav">
    <span class="current" style="left:0">HOME</span>
    <span style="left:59px">BATH TOWELS</span>
    <span style="left:159px">ROBES</span>
    <span style="left:221px">ACCESSORIES</span>
    <span style="left:319px">MATS</span>
    <span style="left:373px">POOL</span>
    <span style="left:432px">BEACH</span>
    <span style="left:495px">BLANKETS &amp; THROWS</span>
    <span style="left:630px">MASSAGE &amp; SAUNA</span>
    <span style="left:753px">NEW COLLECTION</span>
  </nav>
  <div class="abs rule-dash" style="top:140px"></div>
</header>

<section class="abs hero" role="img" aria-label="Textured terry towel draped over a wooden lounger on a rocky seashore, with a woven basket">
  <div class="cloth"></div>
  <span class="line1">Wrap Yourself in</span>
  <span class="line2">Luxury</span>
</section>

<h2 class="abs intro-title">Here at The Harlow Reserve</h2>
<p class="abs intro-text">Here at The Harlow Reserve we deliver the finest in cotton towels, loungewear, and bath accessories to ensure that your bath and spa collection not only looks great, but also offers supreme comfort, absorbency, and durability. By combining quality, lightweight fibers and luxurious weaves, The Harlow Reserve allows you to transform your bathroom, spa, or poolside into a true retreat.</p>

<svg class="abs divider" style="top:746px" viewBox="0 0 710 14" aria-hidden="true">
  <path d="M0 6 H347 L354 12 L361 6 H710" fill="none" stroke="#cadf82" stroke-width="2"/>
</svg>

<div class="abs explore"><span class="small">Explore our</span><span class="big">Textures</span></div>

<section class="textures">
  <span class="arrow" style="left:133px">&lt;</span>
  <div class="tile t1" role="img" aria-label="Close-up banner of green ribbed terry texture"></div>
  <div class="tile t2" role="img" aria-label="Close-up banner of apricot herringbone weave"></div>
  <div class="tile t3" role="img" aria-label="Close-up banner of soft blush waffle texture"></div>
  <div class="tile t4" role="img" aria-label="Close-up banner of orange terry loop texture"></div>
  <span class="arrow" style="left:881px">&gt;</span>
</section>

<svg class="abs divider" style="top:955px" viewBox="0 0 710 14" aria-hidden="true">
  <path d="M0 7 H347 L354 12 L361 7 H710" fill="none" stroke="#cadf82" stroke-width="2"/>
</svg>
<section class="partners">
  <span style="left:224px">The Calloway</span>
  <span style="left:366px">Meridian Vale</span>
  <span style="left:500px">Solmara Resort</span>
  <span style="left:660px">The Ashgrove</span>
</section>
<svg class="abs divider" style="top:1050px" viewBox="0 0 710 14" aria-hidden="true">
  <path d="M0 6 H347 L354 1 L361 6 H710" fill="none" stroke="#cadf82" stroke-width="2"/>
</svg>

<footer class="abs footer">
  <span class="link" style="left:19px">SIGN IN OR REGISTER</span>
  <span class="link" style="left:150px">MY HARLOW</span>
  <span class="link" style="left:241px">MY WISH LIST</span>
  <span class="social" style="left:342px" role="img" aria-label="social link"></span>
  <span class="social" style="left:370px" role="img" aria-label="social link"></span>
  <span class="social" style="left:399px" role="img" aria-label="social link"></span>
  <span class="social" style="left:427px" role="img" aria-label="social link"></span>
  <span class="social" style="left:455px" role="img" aria-label="social link"></span>
  <address>418 Linden Quay, Harbor City, FL 30917<br>Phone: (555) 014-2290, Fax: (555) 014-7730,<br>contact@harlowreserve-example.com</address>
</footer>

</body>
</html>
```